illustration of the importance of using your money as voting power for the environment

Illustration to read either per word, or creative interpretation (open to suggestions) " Vote, use your $ to vote for your favourite candidate" and then below it will have two choices the first reading "Berries- imported (yes), regulated (questionable), Free trade over Free Health (absolutely)" second choice reading "Berries- local (yes), organic (hopefully), regulated (most definatley) Free trade over Free Health (not on Australia's watch). there will be a little thought bubble next to the second choice that says "I know we cost more, but do you think people will get it yet?). It must have my logo on the bottom. I have uploaded the file.

The project is about using your money or your wallet to make a choice, making that choice is equal to voting. Every time you buy something, you are voting for a 'good' project, one that is environmentally friendly and gives positvely to the environment OR you are voting/buying a 'bad' product that is unsustainable, potentially poisonous and damages people and the environment. We just had a health scare here becuase of imported berries that were not regulated because of our new free trade agreement with china, although this is not about china, its about be aware as a consumer and making or Voting for your future.

Target Market(s)

20's- 50's

Industry/Entity Type

Environment

Requirements
Must have
• my logo and business name

```html
<!DOCTYPE html>
<html lang="en">
<head>
<meta charset="utf-8">
<title>Vote With Your Dollars</title>
<link rel="stylesheet" href="https://fonts.googleapis.com/css2?family=Open+Sans:wght@600;700;800&family=Didact+Gothic&display=swap">
<style>
  :root {
    --teal: #45bfb8;
    --teal-text: #43c0b8;
    --mist: #ececec;
    --olive: #c9c95f;
    --slate: #5b5b5b;
    --white: #ffffff;
    --ink: #1e1e1e;
  }
  html, body {
    margin: 0;
    padding: 0;
    overflow: hidden;
    background: var(--teal);
  }
  .poster {
    position: relative;
    width: 1200px;
    height: 898px;
    overflow: hidden;
    background: var(--teal);
    font-family: "Open Sans", Arial, sans-serif;
  }
  .poster svg, .poster .text {
    position: absolute;
  }
  .header-band { left: 0; top: 0; }
  .headline-word {
    position: absolute;
    left: 436px;
    top: 30px;
    margin: 0;
    font-size: 222px;
    line-height: 1;
    font-weight: 700;
    letter-spacing: -4px;
    color: var(--teal-text);
  }
  .ballot-mark { left: 270px; top: 0; }
  .call-out {
    position: absolute;
    left: 89px;
    top: 300px;
    margin: 0;
    font-family: "Didact Gothic", Arial, sans-serif;
    color: var(--slate);
    font-weight: 400;
    line-height: 1;
  }
  .call-out .cap-large { font-size: 73px; }
  .call-out .cap-small { font-size: 54px; }
  .call-out .sub-line {
    display: block;
    margin-top: 6px;
    font-size: 36px;
    letter-spacing: 2px;
  }
  .dollars {
    position: absolute;
    left: 292px;
    top: 318px;
    margin: 0;
    font-size: 112px;
    font-weight: 800;
    line-height: 1;
    letter-spacing: -2px;
    color: var(--olive);
  }
  .tagline {
    position: absolute;
    left: 89px;
    top: 500px;
    margin: 0;
    font-family: "Didact Gothic", Arial, sans-serif;
    font-size: 32px;
    letter-spacing: 2.4px;
    color: var(--slate);
    line-height: 1;
  }
  .choice-label {
    position: absolute;
    margin: 0;
    font-size: 29px;
    font-weight: 600;
    line-height: 1.3;
    color: var(--white);
  }
  .tick-box { position: absolute; }
  .thought-bubble { left: 740px; top: 225px; }
  .page-curl { right: 0; bottom: 0; }
  .brand {
    position: absolute;
    right: 10px;
    bottom: 8px;
    display: flex;
    align-items: center;
    gap: 4px;
    font-size: 13px;
    font-weight: 700;
    color: var(--ink);
  }
  .brand-dot {
    width: 10px;
    height: 10px;
    border-radius: 50%;
    background: var(--ink);
  }
</style>
</head>
<body>
<main class="poster">

  <svg class="header-band" width="1200" height="300" viewBox="0 0 1200 300" aria-hidden="true">
    <path d="M0 0 H1200 V120 C1015 254 761 292 571 285 C317 279 127 228 0 203 Z" fill="var(--mist)"/>
  </svg>

  <svg class="ballot-mark" width="230" height="250" viewBox="0 0 230 250" aria-hidden="true">
    <rect x="32" y="56" width="130" height="186" fill="none" stroke="var(--olive)" stroke-width="4"/>
    <rect x="20" y="44" width="130" height="186" fill="none" stroke="var(--olive)" stroke-width="4"/>
    <path d="M22 122 L58 108 L82 160 L182 8 L222 42 L92 222 Z" fill="var(--olive)"/>
  </svg>
  <h1 class="headline-word">OTE</h1>

  <p class="call-out">
    <span class="cap-large">V</span><span class="cap-small">OTE,</span>
    <span class="sub-line">USE YOUR</span>
  </p>
  <p class="dollars">$$$</p>
  <p class="tagline">TO VOTE FOR OUR FAVORITE CANDIDATE</p>

  <p class="choice-label" style="left:101px; top:607px;">Berries Imported</p>
  <p class="choice-label" style="left:103px; top:682px;">Regulated</p>
  <p class="choice-label" style="left:101px; top:752px;">Free trade over<br>free health</p>

  <p class="choice-label" style="left:590px; top:607px;">Berries local</p>
  <p class="choice-label" style="left:594px; top:682px;">Organic</p>
  <p class="choice-label" style="left:590px; top:752px;">Regulated</p>

  <svg class="tick-box" style="left:392px; top:596px;" width="72" height="60" viewBox="0 0 72 60" aria-label="Yes">
    <rect x="3" y="10" width="46" height="46" fill="none" stroke="var(--white)" stroke-width="3"/>
    <path d="M12 32 L20 26 L28 38 L56 4 L66 12 L29 52 Z" fill="var(--white)" stroke="var(--ink)" stroke-width="2" stroke-linejoin="round"/>
  </svg>
  <svg class="tick-box" style="left:395px; top:682px;" width="52" height="56" viewBox="0 0 52 56" aria-label="Questionable">
    <rect x="3" y="3" width="44" height="48" fill="none" stroke="var(--white)" stroke-width="3"/>
    <text x="25" y="42" text-anchor="middle" font-family="Open Sans, sans-serif" font-weight="800" font-size="38" fill="var(--white)" stroke="var(--ink)" stroke-width="1.5">?</text>
  </svg>
  <svg class="tick-box" style="left:392px; top:752px;" width="72" height="60" viewBox="0 0 72 60" aria-label="Absolutely">
    <rect x="3" y="10" width="46" height="46" fill="none" stroke="var(--white)" stroke-width="3"/>
    <path d="M12 32 L20 26 L28 38 L56 4 L66 12 L29 52 Z" fill="var(--white)" stroke="var(--ink)" stroke-width="2" stroke-linejoin="round"/>
  </svg>

  <svg class="tick-box" style="left:860px; top:588px;" width="72" height="60" viewBox="0 0 72 60" aria-label="Yes">
    <rect x="3" y="10" width="46" height="46" fill="none" stroke="var(--white)" stroke-width="3"/>
    <path d="M12 32 L20 26 L28 38 L56 4 L66 12 L29 52 Z" fill="var(--white)" stroke="var(--ink)" stroke-width="2" stroke-linejoin="round"/>
  </svg>
  <svg class="tick-box" style="left:860px; top:660px;" width="72" height="60" viewBox="0 0 72 60" aria-label="Hopefully">
    <rect x="3" y="10" width="46" height="46" fill="none" stroke="var(--white)" stroke-width="3"/>
    <path d="M12 32 L20 26 L28 38 L56 4 L66 12 L29 52 Z" fill="var(--white)" stroke="var(--ink)" stroke-width="2" stroke-linejoin="round"/>
  </svg>
  <svg class="tick-box" style="left:860px; top:728px;" width="72" height="60" viewBox="0 0 72 60" aria-label="Most definitely">
    <rect x="3" y="10" width="46" height="46" fill="none" stroke="var(--white)" stroke-width="3"/>
    <path d="M12 32 L20 26 L28 38 L56 4 L66 12 L29 52 Z" fill="var(--white)" stroke="var(--ink)" stroke-width="2" stroke-linejoin="round"/>
  </svg>

  <svg class="thought-bubble" width="370" height="360" viewBox="0 0 370 360" aria-label="Thought bubble">
    <g fill="var(--olive)">
      <ellipse cx="190" cy="170" rx="160" ry="120"/>
      <circle cx="110" cy="95" r="70"/>
      <circle cx="200" cy="70" r="60"/>
      <circle cx="280" cy="105" r="65"/>
      <circle cx="315" cy="190" r="50"/>
      <circle cx="270" cy="255" r="62"/>
      <circle cx="170" cy="265" r="60"/>
      <circle cx="75" cy="215" r="62"/>
      <circle cx="45" cy="145" r="45"/>
      <path d="M205 300 L228 348 L250 290 Z"/>
    </g>
    <g transform="rotate(17 190 170)" font-family="Open Sans, sans-serif" font-weight="600" font-size="31" fill="var(--white)" text-anchor="middle">
      <text x="180" y="105">I know we</text>
      <text x="190" y="150">cost more but do you</text>
      <text x="190" y="195">think people will</text>
      <text x="190" y="240">get it yet?</text>
    </g>
  </svg>

  <svg class="page-curl" width="120" height="120" viewBox="0 0 120 120" aria-hidden="true">
    <path d="M120 0 C100 60 70 100 0 120 H120 Z" fill="var(--white)"/>
    <path d="M120 0 C104 55 76 96 12 118 C70 104 104 70 120 20 Z" fill="#d6d6d6"/>
  </svg>
  <div class="brand"><span class="brand-dot"></span>Buywise</div>

</main>
</body>
</html>
```